New Poster Design for Film Festival

Hi! We need a poster design for our student film festival and the Harlow Ridge University. We screen over 300 short films over a 3 days in May. Our committee wants a look feel similar to the image we attached below.

Target Market(s)

Students and general audience.

Industry/Entity Type

Festival

Colors
3377b5
85abd2
34b8a4
f68e4e

Requirements
Must have
• Otters Film Festival
17th Annual
May 2-3-4 2014
Ned Varrow Cinema
Free Admission
Department of Screen and Digital Narrative

Poster size 36" (high) x 24" (wide)
Harlow Ridge University
www.ottersfilmfest.example
Nice to have
• Bold lettering
Should not have
• Flamingos - hate them :)

```html
<!DOCTYPE html>
<html lang="en">
<head>
<meta charset="utf-8">
<title>Otters Film Festival — 17th Annual Poster</title>
<link rel="stylesheet" href="https://fonts.googleapis.com/css2?family=Bowlby+One&family=Oswald:wght@400;500&family=Arimo:wght@700&display=swap">
<style>
  :root {
    --page-bg: #f1f1f1;
    --page-edge: #e2e2e2;
    --sea-teal: #79a9b5;
    --festival-orange: #f68e4e;
    --festival-blue: #3377b5;
    --soft-blue: #85abd2;
    --paper-white: #ffffff;
  }
  html, body {
    margin: 0;
    padding: 0;
    width: 1200px;
    height: 1000px;
    overflow: hidden;
  }
  body {
    background: radial-gradient(ellipse at center, var(--page-bg) 55%, var(--page-edge) 100%);
    position: relative;
  }
  .poster {
    position: absolute;
    left: 294px;
    top: 39px;
    width: 612px;
    height: 922px;
    box-shadow: 0 2px 6px rgba(0,0,0,0.12);
  }
  .poster svg { display: block; }
  .headline {
    font-family: "Bowlby One", "Arial Black", sans-serif;
    fill: var(--paper-white);
  }
  .event-details {
    font-family: "Oswald", "Arial Narrow", sans-serif;
    font-weight: 500;
    font-size: 24px;
    fill: var(--paper-white);
  }
  .web-address {
    font-family: "Arimo", Arial, sans-serif;
    font-weight: 700;
    font-size: 26px;
    fill: var(--festival-blue);
  }
</style>
</head>
<body>
  <div class="poster">
    <svg width="612" height="922" viewBox="0 0 612 922" xmlns="http://www.w3.org/2000/svg">
      <defs>
        <clipPath id="poster-bounds"><rect width="612" height="922"/></clipPath>
        <linearGradient id="palm-tone" x1="0" y1="0" x2="0" y2="1">
          <stop offset="0" stop-color="#ffffff" stop-opacity="0.35"/>
          <stop offset="1" stop-color="#3377b5" stop-opacity="0.35"/>
        </linearGradient>
        <linearGradient id="skyline-tone" x1="0" y1="0" x2="0" y2="1">
          <stop offset="0" stop-color="#ffffff" stop-opacity="0"/>
          <stop offset="0.6" stop-color="#ffffff" stop-opacity="0.9"/>
          <stop offset="1" stop-color="#ffffff" stop-opacity="1"/>
        </linearGradient>
      </defs>

      <g clip-path="url(#poster-bounds)">
        <rect class="backdrop" width="612" height="922" fill="var(--sea-teal)"/>

        <rect class="palm-top" x="456" y="28" width="156" height="218" rx="60"
              fill="url(#palm-tone)" role="img" aria-label="Stylised palm tree illustration"/>
        <rect class="palm-left" x="4" y="442" width="228" height="404" rx="80"
              fill="url(#palm-tone)" role="img" aria-label="Stylised palm tree with swirling trunk illustration"/>

        <circle class="title-disc" cx="195" cy="85" r="230" fill="var(--festival-orange)" stroke="var(--paper-white)" stroke-width="4"/>
        <text class="headline" x="30" y="86" font-size="68" textLength="320" lengthAdjust="spacingAndGlyphs">OTTERS</text>
        <text class="headline" x="69" y="174" font-size="95" textLength="252" lengthAdjust="spacingAndGlyphs">FILM</text>
        <text class="headline" x="36" y="239" font-size="62" textLength="314" lengthAdjust="spacingAndGlyphs">FESTIVAL</text>
        <g class="title-dots" fill="var(--paper-white)">
          <rect x="131" y="270" width="26" height="16" rx="3"/>
          <rect x="171" y="270" width="26" height="16" rx="3"/>
          <rect x="211" y="270" width="26" height="16" rx="3"/>
        </g>

        <circle class="edition-disc" cx="439" cy="398" r="180" fill="var(--festival-blue)" stroke="var(--paper-white)" stroke-width="6"/>
        <text class="headline" x="316" y="459" font-size="200" textLength="200" lengthAdjust="spacingAndGlyphs">17</text>
        <text class="headline" x="518" y="459" font-size="60" textLength="64" lengthAdjust="spacingAndGlyphs">th</text>
        <text class="headline" x="316" y="517" font-size="52" textLength="269" lengthAdjust="spacingAndGlyphs">ANNUAL</text>

        <g class="event-details">
          <text x="355" y="642">May 2-3-4 2014</text>
          <text x="355" y="673">Ned Varrow Cinema</text>
          <text x="355" y="704">Department of Screen</text>
          <text x="355" y="735">and Digital Narrative</text>
          <text x="355" y="765">Harlow Ridge University</text>
          <text x="355" y="796">FREE ADMISSION</text>
        </g>

        <rect class="skyline" x="0" y="786" width="612" height="80"
              fill="url(#skyline-tone)" role="img" aria-label="City skyline silhouette"/>
        <rect class="footer-band" x="0" y="862" width="612" height="60" fill="var(--paper-white)"/>
        <text class="web-address" x="306" y="905" text-anchor="middle" textLength="425" lengthAdjust="spacingAndGlyphs">www.ottersfilmfest.example</text>
      </g>
    </svg>
  </div>
</body>
</html>
```